Reputable business cards for Diplom Kauffrau, Privat und Geschäftslich

The business cards should be reputable, valuable and elegant in order to be able to use them for business. The design should also include a sophistication that is conspicuous. This could be a picture, an ornament, a sublime print or a kind of logo of the initials of my name "MD". The font should be clear and legible.
Target Market(s)
Business contacts, friends and acquaintances
Contact Information for Business Card
Diplom-Kauffrau Mirela Donat
Lindenhofweg 7 50931 Kerpen
Mobil +49 171 804 29 57
e-mail mirela.donat@postwerk.de
Colors
Designer to choose colors to be used in the design.
Requirements
Must have
- Clear and easy to read font My name in larger font than the other information Visual conspicuity / specificity
Nice to have
- Different colors
Should not have
- Ornate font, playful

```html
<!DOCTYPE html>
<html lang="de">
<head>
<meta charset="utf-8">
<title>Mirela Donat – Visitenkarten</title>
<link href="https://fonts.googleapis.com/css2?family=Poppins:wght@600&family=Lato:wght@400&display=swap" rel="stylesheet">
<style>
  :root {
    --stage: #2b2b2c;
    --card-dark: #333334;
    --brand-red: #d90d3a;
    --ink-light: #f2f2f2;
    --ink-muted: #8a8a8a;
    --rule: #6a6a6a;
  }
  * { margin: 0; padding: 0; box-sizing: border-box; }
  html, body { width: 1200px; height: 866px; overflow: hidden; }
  body {
    background: var(--stage);
    display: flex;
    align-items: center;
    justify-content: center;
    gap: 48px;
    font-family: "Lato", sans-serif;
  }
  .card {
    position: relative;
    width: 520px;
    height: 336px;
    box-shadow: 0 14px 30px rgba(0,0,0,.45);
  }
  /* front */
  .card--front {
    background: var(--brand-red);
    display: flex;
    align-items: center;
    justify-content: center;
    gap: 18px;
  }
  .front-dot {
    width: 54px; height: 54px;
    border-radius: 50%;
    background: var(--ink-light);
  }
  .front-name {
    font-family: "Poppins", sans-serif;
    font-weight: 600;
    font-size: 34px;
    color: var(--ink-light);
    letter-spacing: .5px;
  }
  /* back */
  .card--back {
    background: var(--card-dark);
    color: var(--ink-light);
    overflow: hidden;
  }
  .card--back::after {
    content: "";
    position: absolute;
    left: 0; right: 0; bottom: 0;
    height: 9px;
    background: var(--brand-red);
  }
  .contact {
    position: absolute;
    left: 30px;
    top: 118px;
    width: 200px;
    border-top: 1px solid var(--rule);
    padding-top: 18px;
    font-size: 14px;
    line-height: 1.55;
  }
  .contact-line { display: flex; align-items: center; gap: 8px; }
  .contact-line svg { width: 12px; height: 12px; flex: none; }
  .identity {
    position: absolute;
    right: 30px;
    top: 34px;
    width: 250px;
    text-align: right;
  }
  .identity-dot {
    display: inline-block;
    width: 84px; height: 84px;
    border-radius: 50%;
    background: var(--brand-red);
    margin-right: 6px;
  }
  .identity-name {
    font-family: "Poppins", sans-serif;
    font-weight: 600;
    font-size: 27px;
    line-height: 1.1;
    margin-top: 14px;
    letter-spacing: .3px;
  }
  .identity-title {
    font-family: "Poppins", sans-serif;
    font-weight: 600;
    font-size: 8px;
    letter-spacing: 3.4px;
    color: var(--ink-muted);
    margin-top: 3px;
  }
  .address {
    border-top: 1px solid var(--rule);
    margin-top: 16px;
    padding-top: 12px;
    font-size: 15px;
    line-height: 1.35;
  }
</style>
</head>
<body>
  <section class="card card--back" aria-label="Rückseite der Visitenkarte">
    <div class="contact">
      <p class="contact-line">
        <svg viewBox="0 0 12 12" aria-hidden="true"><path fill="#d90d3a" d="M1 3.5C1 2 2.5 1 6 1s5 1 5 2.5V5H8.5V3.8h-5V5H1zM3 6h6l1.5 5h-9z"/></svg>
        +49 171 804 29 57
      </p>
      <p class="contact-line">
        <svg viewBox="0 0 12 12" aria-hidden="true"><rect x="0.5" y="2" width="11" height="8" fill="#d90d3a"/><path d="M1 2.6 6 6.6l5-4" fill="none" stroke="#333334" stroke-width="1"/></svg>
        mirela.donat@postwerk.de
      </p>
    </div>
    <div class="identity">
      <span class="identity-dot" aria-hidden="true"></span>
      <h1 class="identity-name">Mirela Donat</h1>
      <p class="identity-title">DIPLOM-KAUFFRAU</p>
      <p class="address">Lindenhofweg 7<br>50931 Kerpen</p>
    </div>
  </section>

  <section class="card card--front" aria-label="Vorderseite der Visitenkarte">
    <span class="front-dot" aria-hidden="true"></span>
    <span class="front-name">Mirela Donat</span>
  </section>
</body>
</html>
```